IT Company requires new Business Card design.

Over the years we have had a few different business card designs. We are now due for new cards across the board for all staff. We felt this would be a good time to start fresh with a new design. Our traditional card simply had our details on the front, and a list of services on the back. We don't particularly need the list of services, we have had cards where the only thing on the rear of the card was our logo.
Feel free to be creative, we would like our tag line "Complete IT Management" to appear at some point, doesn't necessarily have to be with the logo.
I have attached samples and drafts of various previous cards we have used over the years.

```html
<!DOCTYPE html>
<html lang="en">
<head>
<meta charset="utf-8">
<title>Ridgeway Networking – Business Card</title>
<link rel="stylesheet" href="https://fonts.googleapis.com/css2?family=Arimo:wght@400;700&family=Archivo:wght@800&family=Open+Sans:wght@400;600&display=swap">
<style>
  :root {
    --stage: #2c2d30;
    --card-white: #ffffff;
    --card-grey: #dfe2e6;
    --brand-blue: #3f7fc0;
    --name-blue: #2a5bab;
    --ink-blue: #1f4f8f;
    --slate: #4a5763;
    --text-grey: #5a6470;
    --band-blue: #2a62b4;
    --band-slate: #56636f;
    --back-slate: #3a4f66;
    --back-blue: #1f6bb9;
    --white: #ffffff;
  }
  * { box-sizing: border-box; margin: 0; padding: 0; }
  html, body { width: 1057px; height: 1200px; overflow: hidden; background: var(--stage); }
  .canvas { position: relative; width: 1057px; height: 1200px; }

  .card { position: absolute; left: 129px; width: 822px; height: 472px; overflow: hidden; }
  .card--front {
    top: 56px;
    background: radial-gradient(ellipse at 40% 40%, var(--card-white) 35%, var(--card-grey) 100%);
  }
  .card--back {
    top: 602px;
    background: linear-gradient(90deg, var(--back-slate) 0%, #2f5c8e 45%, var(--back-blue) 100%);
  }

  .lockup { position: absolute; display: flex; align-items: center; gap: 22px; }
  .lockup__mark { width: 112px; height: 112px; flex: none; }
  .lockup__name {
    font-family: "Arimo", Arial, sans-serif; font-weight: 700;
    font-size: 40px; line-height: 1; letter-spacing: 0.5px; text-transform: uppercase;
  }
  .lockup__tagline {
    font-family: "Arimo", Arial, sans-serif; font-weight: 400;
    font-size: 14px; letter-spacing: 2.6px; text-transform: uppercase; margin-top: 6px;
  }

  .card--front .lockup { left: 77px; top: 55px; }
  .card--front .lockup__mark { background: var(--slate); }
  .card--front .lockup__name, .card--front .lockup__tagline { color: var(--brand-blue); }

  .person { position: absolute; left: 77px; top: 270px; }
  .person__name {
    font-family: "Archivo", Arial, sans-serif; font-weight: 800;
    font-size: 28px; color: var(--name-blue); letter-spacing: -0.5px;
  }
  .person__role {
    font-family: "Open Sans", Arial, sans-serif; font-size: 17px; color: var(--text-grey); margin-top: 2px;
  }

  .band { position: absolute; left: 0; top: 350px; width: 822px; height: 38px; }
  .band__address {
    position: absolute; right: 34px; top: 350px; height: 38px; line-height: 38px;
    font-family: "Arimo", Arial, sans-serif; font-size: 18px; color: var(--white);
  }

  .contacts { position: absolute; left: 78px; top: 403px; display: flex; gap: 28px; align-items: center; }
  .contact { display: flex; align-items: center; gap: 8px;
    font-family: "Open Sans", Arial, sans-serif; font-weight: 600; font-size: 19px; color: var(--ink-blue); }
  .contact svg { width: 34px; height: 34px; }

  .card--back .lockup { left: 144px; top: 140px; gap: 36px; }
  .card--back .lockup__mark { background: var(--white); width: 150px; height: 150px; }
  .card--back .lockup__name { color: var(--white); font-size: 52px; }
  .card--back .lockup__tagline { color: var(--white); font-size: 17px; letter-spacing: 3.2px; margin-top: 10px; }

  .website {
    position: absolute; left: 0; right: 0; top: 378px; text-align: center;
    font-family: "Arimo", Arial, sans-serif; font-size: 25px; letter-spacing: 4px; color: var(--white);
  }
</style>
</head>
<body>
<main class="canvas">

  <section class="card card--front" aria-label="Business card front">
    <div class="lockup">
      <div class="lockup__mark"></div>
      <div class="lockup__text">
        <div class="lockup__name">Ridgeway<br>Networking</div>
        <div class="lockup__tagline">Complete IT Management</div>
      </div>
    </div>

    <div class="person">
      <div class="person__name">MARCUS HALE</div>
      <div class="person__role">Business Development</div>
    </div>

    <svg class="band" viewBox="0 0 822 38" preserveAspectRatio="none" aria-hidden="true">
      <rect x="0" y="0" width="822" height="3" fill="var(--band-blue)"/>
      <polygon points="0,5 282,5 260,32 0,32" fill="var(--band-blue)"/>
      <polygon points="268,38 296,5 822,5 822,38" fill="var(--band-slate)"/>
    </svg>
    <div class="band__address">Unit 4, 22 Harbour Lane , Westfield, WA 6100</div>

    <div class="contacts">
      <div class="contact">
        <svg viewBox="0 0 34 34" aria-hidden="true">
          <circle cx="17" cy="17" r="15" fill="none" stroke="var(--slate)" stroke-width="2"/>
          <path d="M11 9 l4 0 l1 5 l-2 2 q2 4 5 5 l2 -2 l5 1 l0 4 q-10 1 -15 -15z" fill="var(--slate)"/>
        </svg>
        <span>08 5550 1420</span>
      </div>
      <div class="contact">
        <svg viewBox="0 0 34 34" aria-hidden="true">
          <circle cx="17" cy="17" r="15" fill="none" stroke="var(--slate)" stroke-width="2"/>
          <rect x="12" y="8" width="10" height="6" fill="var(--slate)"/>
          <rect x="9" y="14" width="16" height="9" rx="1" fill="var(--slate)"/>
          <rect x="12" y="20" width="10" height="6" fill="var(--white)" stroke="var(--slate)" stroke-width="1.5"/>
        </svg>
        <span>08 5550 1422</span>
      </div>
      <div class="contact">
        <svg viewBox="0 0 34 34" aria-hidden="true">
          <circle cx="17" cy="17" r="15" fill="none" stroke="var(--slate)" stroke-width="2"/>
          <rect x="9" y="11" width="16" height="12" fill="var(--slate)"/>
          <path d="M9 11 l8 7 l8 -7" fill="none" stroke="var(--white)" stroke-width="1.5"/>
        </svg>
        <span>marcus@ridgewaynet.com.au</span>
      </div>
    </div>
  </section>

  <section class="card card--back" aria-label="Business card back">
    <div class="lockup">
      <div class="lockup__mark"></div>
      <div class="lockup__text">
        <div class="lockup__name">Ridgeway<br>Networking</div>
        <div class="lockup__tagline">Complete IT Management</div>
      </div>
    </div>
    <div class="website">www.ridgewaynet.com.au</div>
  </section>

</main>
</body>
</html>
```